Freshen up Product Labels

We need product label designs refreshed throughout our brand. We will start with the main product as that will set the basic design for most other labels. We are currently using 2.5" wide x 4.5" tall vinyl labels for most products and would like to stick to that size for this project. There are 3 of this size label on a jug of our all natural house cleaning concentrate. Uploaded current design and open to your new ideas. Our products can be found in more detail at quillbrook.com

```html
<!DOCTYPE html>
<html lang="en">
<head>
<meta charset="utf-8">
<title>Quillbrook Aromatherapy Cleaning Concentrate – Labels</title>
<link href="https://fonts.googleapis.com/css2?family=Montserrat:wght@400;500;600&display=swap" rel="stylesheet">
<style>
  :root {
    --backdrop: #666666;
    --label: #ffffff;
    --green: #57b84b;
    --ink: #3a3a3a;
    --white: #ffffff;
  }
  * { margin: 0; padding: 0; box-sizing: border-box; }
  html, body { width: 1200px; height: 2203px; overflow: hidden; }
  body {
    background: var(--backdrop);
    font-family: "Montserrat", Arial, sans-serif;
    color: var(--ink);
    position: relative;
  }
  .label {
    position: absolute;
    top: 615px;
    width: 484px;
    height: 873px;
    background: var(--label);
    transform: scale(1.1157);
    transform-origin: top left;
    overflow: hidden;
  }
  .label--front { left: 40px; }
  .label--back { left: 620px; }
  .abs { position: absolute; }
  .center { left: 0; width: 100%; text-align: center; }

  /* front */
  .seal { left: 344px; top: 42px; width: 96px; height: 96px; border: 2.5px solid var(--green); border-radius: 50%; }
  .brand { top: 160px; display: flex; justify-content: center; align-items: center; gap: 10px; }
  .brand__dot { width: 16px; height: 16px; border-radius: 50%; background: var(--green); }
  .brand__name { font-size: 36px; font-weight: 600; color: var(--green); letter-spacing: 1px; }
  .title { top: 280px; font-size: 43px; font-weight: 500; letter-spacing: 0.5px; }
  .subtitle { top: 338px; font-size: 23px; font-weight: 400; }
  .rule { left: 26px; width: 432px; height: 2px; background: var(--green); }
  .tagline { top: 443px; font-size: 19.5px; }
  .scent-box { left: 26px; top: 498px; width: 432px; height: 122px; background: var(--green); color: var(--white);
    font-size: 24.5px; line-height: 33px; text-align: center; padding-top: 26px; }
  .formula { top: 656px; font-size: 19.5px; }
  .size { top: 745px; font-size: 31px; font-weight: 500; }
  .yield { top: 800px; font-size: 19.5px; }
  .band { left: 26px; top: 835px; width: 432px; height: 38px; background: var(--green); }

  /* back */
  .tab { left: 144px; width: 196px; height: 35px; background: var(--green); }
  .tab--top { top: 0; }
  .tab--bottom { top: 838px; }
  .blurb { left: 28px; top: 70px; width: 428px; font-size: 17px; line-height: 22.3px; text-align: justify; }
  .claims { left: 22px; top: 270px; width: 440px; height: 217px; background: var(--green); border-radius: 28px; color: var(--white); text-align: center; }
  .claims__head { font-size: 18px; font-weight: 600; }
  .claims__list { font-size: 15px; line-height: 21px; }
  .claims__yes { position: absolute; top: 26px; width: 100%; }
  .claims__no { position: absolute; top: 126px; width: 100%; }
  .claims__divider { position: absolute; left: 17px; top: 114px; width: 406px; height: 1px; background: var(--white); }
  .ingredients-head { left: 30px; top: 513px; font-size: 18px; font-weight: 600; color: var(--green); }
  .ingredients { left: 28px; top: 544px; width: 428px; font-size: 17px; line-height: 22.3px; text-align: justify; }
  .warnings { left: 30px; top: 724px; font-size: 16.5px; line-height: 22.3px; }
  .visit { right: 30px; top: 724px; font-size: 16.5px; line-height: 22.3px; text-align: right; }
  .visit strong { color: var(--green); font-weight: 600; }
</style>
</head>
<body>

<section class="label label--front" aria-label="Front label">
  <div class="abs seal" role="img" aria-label="Synthetic-free badge"></div>
  <div class="abs center brand">
    <span class="brand__dot"></span>
    <span class="brand__name">QUILLBROOK</span>
  </div>
  <h1 class="abs center title">AROMATHERAPY</h1>
  <p class="abs center subtitle">CLEANING CONCETRATE</p>
  <div class="abs rule" style="top:402px"></div>
  <p class="abs center tagline">Contains Powerful Essential Oils</p>
  <div class="abs rule" style="top:493px; height:2.5px"></div>
  <div class="abs scent-box">CINAMON + CLOVE + ROSEMARY<br>PEPPEMINT + EUCALYPTUS</div>
  <div class="abs rule" style="top:631px; height:2.5px"></div>
  <p class="abs center formula">Ultra-Concentraded Versatile Formula</p>
  <p class="abs center size">64 oz</p>
  <p class="abs center yield">Makes up to 24 Gallons of Cleaner</p>
  <div class="abs band"></div>
</section>

<section class="label label--back" aria-label="Back label">
  <div class="abs tab tab--top"></div>
  <p class="abs blurb">Turn the mundane task of cleaning into an Aroma-therapy Session while breezing through the house. From kitchen to bath to windows, doors and floors, this all-purpose NATURAL cleaner covers all. Our potent essential oil enriched blend is safe to use in various ratios for virtually any cleaning task in you home. We unconditionally guarantee your sensory and cleaning satisfaction. More at Quillbrook.com</p>
  <div class="abs claims">
    <div class="claims__yes">
      <p class="claims__head">YES</p>
      <p class="claims__list">Non Toxic Family &amp; Earth Friendly Plant Based<br>Natural Ingredients • Multi-purpose</p>
    </div>
    <div class="claims__divider"></div>
    <div class="claims__no">
      <p class="claims__head">NO</p>
      <p class="claims__list">Laurel Sulfates • Preservatives • Phthalates • Dyes<br>Synthetic Fragrance • Vinegar • Chemical Concoctions</p>
    </div>
  </div>
  <p class="abs ingredients-head">Ingredients:</p>
  <p class="abs ingredients">Water, Essential Oils: Cinnamon Leaf (cinnamomum zeylanicum), Clove (eugenia caryo- phyllata), Lemon (citrus limonum), Eucalyptus Globu- lus, Rosemary (rosemarinus officianales), Peppermint (mentha piperita), Sodium Cocoate, Vegetable Glycer- ine, Sodium Chloride, Sodium Gluconate, Citric Acid.</p>
  <p class="abs warnings">Keep out of reach of children.<br>Stop use if irritation occurs.<br>Keep out of eyes.<br>For external use only.</p>
  <p class="abs visit"><strong>Visit</strong><br><strong>quillbrook.com</strong><br>for complete use<br>and dilution guide.</p>
  <div class="abs tab tab--bottom"></div>
</section>

</body>
</html>
```